Redesign website bus travel company Lenz Vals

We require a complete redesign of the website of Reisebüro Lenz Vals, an established bus tour operator based in Graubünden (www.lenzvals-beispiel.ch). For years, the company has specialized in multi-day tours throughout Europe, as well as day trips such as shopping trips to Innsbruck or Como, music tours, and market visits, primarily for seniors, as well as car rentals for clubs and companies.

The new website requires a video header with overlay text, red as the primary corporate color, complemented by black and gray, and a highly simplified navigation with two main sections: "Our Trips" and "Bus Rental." The remaining sections must be accessible via the "Menu" menu item. The design should be user-friendly for all age groups and mobile-responsive.

The goal is a trustworthy, modern website that reflects personal service and many years of experience.
The new logo can be found in the files, as well as a few pictures.

Target Market(s)

Guests of bus tours (day and multi-day trips) and bus rentals (clubs, companies, etc.)

Industry/Entity Type

Busreisen und Busvermietung

Number of Pages Required

1 page

Requirements
Must have
• Red as primary color, video header, simple UX for target group seniors
Nice to have
• Photo galleries of destinations and the vehicle fleet

```html
<!DOCTYPE html>
<html lang="en">
<head>
<meta charset="utf-8">
<title>Reisebüro Lenz Vals – Bus Tours &amp; Bus Rental</title>
<link href="https://fonts.googleapis.com/css2?family=Inter:wght@400;500;600;700;800&display=swap" rel="stylesheet">
<style>
:root{
  --red:#e0262b;
  --red-dark:#c21d22;
  --ink:#1f2430;
  --text:#4a5160;
  --muted:#7b8190;
  --line:#e6e8ec;
  --soft:#f4f5f7;
  --white:#ffffff;
  --footer:#333a48;
  --footer-text:#aeb4c0;
}
*{box-sizing:border-box;margin:0;padding:0}
html,body{width:1200px;height:2960px;overflow:hidden}
body{font-family:"Inter",Arial,sans-serif;color:var(--text);background:var(--white);font-size:14px}
a{color:inherit;text-decoration:none}
.btn{display:inline-block;background:var(--red);color:#fff;font-weight:600;font-size:13px;padding:11px 22px;border-radius:4px;text-align:center}
.btn-light{background:#fff;color:var(--ink)}
.btn-block{display:block;width:100%}
.section{position:relative}
.section-title{text-align:center;font-size:36px;font-weight:700;color:var(--ink)}
.section-sub{text-align:center;font-size:14px;color:var(--muted);margin-top:10px}

/* header */
.site-header{height:44px;display:flex;align-items:center;justify-content:space-between;padding:0 40px;background:#fff;box-shadow:0 1px 4px rgba(0,0,0,.08);position:relative;z-index:2}
.brand{display:flex;align-items:center;gap:8px;font-weight:800;font-size:16px;color:var(--red)}
.brand-mark{width:14px;height:14px;background:var(--red);border-radius:50%}
.main-nav{display:flex;align-items:center;gap:26px;font-size:13px;font-weight:500;color:var(--ink)}
.main-nav .btn{padding:8px 16px;font-size:12px}

/* hero */
.hero{height:676px;position:relative;display:flex;flex-direction:column;align-items:center;justify-content:center;text-align:center;color:#fff}
.hero-media{position:absolute;inset:0;background:linear-gradient(180deg,#6d7f8c 0%,#8a9aa0 30%,#5d7040 62%,#3f5a2a 100%)}
.hero-media::after{content:"";position:absolute;inset:0;background:rgba(0,0,0,.35)}
.hero-content{position:relative;margin-top:-40px}
.hero h1{font-size:60px;font-weight:800;line-height:1.1}
.hero p{font-size:17px;max-width:720px;margin:18px auto 26px;line-height:1.5}
.hero-actions{display:flex;gap:14px;justify-content:center}
.hero-dots{position:absolute;bottom:20px;left:50%;transform:translateX(-50%);width:16px;height:16px;border:2px solid #fff;border-radius:50%}

/* services */
.services{height:520px;background:var(--soft);padding-top:52px}
.service-grid{display:grid;grid-template-columns:1fr 1fr;gap:24px;width:640px;margin:34px auto 0}
.service-card{background:#fff;border-radius:8px;padding:26px 26px 22px;box-shadow:0 2px 10px rgba(0,0,0,.06)}
.service-icon{width:44px;height:44px;border-radius:50%;background:#fde5e6;display:flex;align-items:center;justify-content:center;margin:0 auto 12px}
.service-card h3{text-align:center;font-size:17px;color:var(--ink)}
.service-card .lead{text-align:center;font-size:12px;color:var(--muted);margin:6px 0 16px}
.service-list{list-style:none;margin-bottom:18px}
.service-list li{display:flex;gap:8px;align-items:center;font-size:12.5px;padding:5px 0}
.service-list svg{flex:none}

/* destinations */
.destinations{height:360px;padding-top:52px}
.dest-grid{display:grid;grid-template-columns:repeat(4,1fr);gap:20px;width:880px;margin:34px auto 0}
.dest-card{position:relative;height:200px;border-radius:8px;overflow:hidden;color:#fff}
.dest-card .media{position:absolute;inset:0}
.dest-card::after{content:"";position:absolute;inset:0;background:linear-gradient(180deg,rgba(0,0,0,0) 55%,rgba(0,0,0,.65))}
.dest-card span{position:absolute;left:14px;bottom:14px;font-weight:700;font-size:14px;z-index:1}

/* fleet */
.fleet{height:360px;background:var(--soft);padding-top:52px}
.fleet-grid{display:grid;grid-template-columns:1fr 1fr;gap:20px;width:560px;margin:34px auto 0}
.fleet-card{position:relative;height:170px;border-radius:8px;overflow:hidden;color:#fff}
.fleet-card .media{position:absolute;inset:0}
.fleet-card::after{content:"";position:absolute;inset:0;background:linear-gradient(180deg,rgba(0,0,0,0) 45%,rgba(0,0,0,.7))}
.fleet-card .caption{position:absolute;left:14px;bottom:12px;z-index:1}
.fleet-card strong{display:block;font-size:14px}
.fleet-card small{font-size:11px;opacity:.85}

/* testimonials */
.testimonials{height:340px;padding-top:52px}
.quote-grid{display:grid;grid-template-columns:repeat(3,1fr);gap:22px;width:880px;margin:34px auto 0}
.quote-card{background:var(--soft);border-radius:8px;padding:20px}
.stars{display:flex;gap:3px;margin-bottom:10px}
.quote-card p{font-size:12.5px;font-style:italic;line-height:1.55;color:var(--text)}
.quote-card .author{margin-top:14px;font-size:12.5px;font-weight:700;color:var(--ink)}
.quote-card .place{font-size:11px;color:var(--muted)}

/* contact */
.contact{height:420px;background:var(--soft);padding-top:52px}
.contact-grid{display:grid;grid-template-columns:1fr 1fr;gap:24px;width:880px;margin:34px auto 0}
.contact-card{background:#fff;border-radius:8px;padding:24px 24px 22px;box-shadow:0 2px 10px rgba(0,0,0,.05);height:232px}
.contact-card h3{font-size:17px;color:var(--ink);margin-bottom:16px}
.hours-row{display:flex;justify-content:space-between;font-size:12.5px;padding:7px 0;border-bottom:1px solid var(--line)}
.hours-row b{color:var(--ink);font-weight:600}
.notice{margin-top:14px;font-size:12px;font-weight:600;color:var(--red)}
.contact-card .btn-small{margin-top:8px;padding:8px 14px;font-size:12px}
.info-item{margin-bottom:10px;font-size:12.5px;line-height:1.45}
.info-item b{display:block;color:var(--ink);font-weight:600}

/* footer */
.site-footer{height:240px;background:var(--footer);color:var(--footer-text);padding:44px 160px 0}
.footer-grid{display:grid;grid-template-columns:1.6fr 1fr 1fr 1fr;gap:30px}
.footer-brand .brand{color:#fff;margin-bottom:10px}
.footer-brand .brand-mark{background:var(--red)}
.footer-grid p,.footer-grid li{font-size:12px;line-height:1.7}
.footer-grid h4{color:#fff;font-size:13px;margin-bottom:8px}
.footer-grid ul{list-style:none}
.copyright{border-top:1px solid rgba(255,255,255,.12);margin-top:34px;padding-top:18px;text-align:center;font-size:11.5px}
</style>
</head>
<body>

<header class="site-header">
  <a class="brand" href="#"><span class="brand-mark"></span>Lenz Vals</a>
  <nav class="main-nav">
    <a href="#">Our Tours</a>
    <a href="#">Bus Rental</a>
    <a href="#">Menu</a>
    <a class="btn" href="#">Request Quote</a>
  </nav>
</header>

<section class="hero">
  <div class="hero-media" role="img" aria-label="Video header: couple in traditional costume with accordion in an alpine meadow beside a touring coach"></div>
  <div class="hero-content">
    <h1>Your Dream Trip Starts Here</h1>
    <p>For over fifty years we have been bringing travellers from Graubünden safely and comfortably to the most beautiful destinations in Europe.</p>
    <div class="hero-actions">
      <a class="btn" href="#">Discover Our Tours</a>
      <a class="btn btn-light" href="#">Rent a Bus</a>
    </div>
  </div>
  <span class="hero-dots"></span>
</section>

<section class="section services">
  <h2 class="section-title">Our Services</h2>
  <p class="section-sub">From day trips to multi-day tours – we bring you safely and comfortably to your destination.</p>
  <div class="service-grid">
    <article class="service-card">
      <div class="service-icon">
        <svg width="20" height="20" viewBox="0 0 24 24" fill="none" stroke="#e0262b" stroke-width="2"><circle cx="12" cy="10" r="3"/><path d="M12 21s-7-6.5-7-11a7 7 0 0 1 14 0c0 4.5-7 11-7 11z"/></svg>
      </div>
      <h3>Our Tours</h3>
      <p class="lead">Discover Europe with our experienced tour guides</p>
      <ul class="service-list">
        <li><svg width="14" height="14" viewBox="0 0 24 24" fill="none" stroke="#e0262b" stroke-width="2.5"><rect x="3" y="3" width="18" height="18" rx="3"/><path d="M8 12l3 3 5-6"/></svg>Day trips (Shopping, Markets)</li>
        <li><svg width="14" height="14" viewBox="0 0 24 24" fill="none" stroke="#e0262b" stroke-width="2.5"><rect x="3" y="3" width="18" height="18" rx="3"/><path d="M8 12l3 3 5-6"/></svg>Multi-day tours Europe</li>
        <li><svg width="14" height="14" viewBox="0 0 24 24" fill="none" stroke="#e0262b" stroke-width="2.5"><rect x="3" y="3" width="18" height="18" rx="3"/><path d="M8 12l3 3 5-6"/></svg>Music tours &amp; cultural trips</li>
        <li><svg width="14" height="14" viewBox="0 0 24 24" fill="none" stroke="#e0262b" stroke-width="2.5"><rect x="3" y="3" width="18" height="18" rx="3"/><path d="M8 12l3 3 5-6"/></svg>Specially designed for seniors</li>
      </ul>
      <a class="btn btn-block" href="#">View Tour Program</a>
    </article>
    <article class="service-card">
      <div class="service-icon">
        <svg width="20" height="20" viewBox="0 0 24 24" fill="none" stroke="#e0262b" stroke-width="2"><rect x="4" y="3" width="16" height="14" rx="2"/><path d="M4 11h16"/><circle cx="8" cy="19" r="1.5"/><circle cx="16" cy="19" r="1.5"/></svg>
      </div>
      <h3>Bus Rental</h3>
      <p class="lead">Professional transport solutions for your group</p>
      <ul class="service-list">
        <li><svg width="14" height="14" viewBox="0 0 24 24" fill="none" stroke="#e0262b" stroke-width="2.5"><rect x="3" y="3" width="18" height="18" rx="3"/><path d="M8 12l3 3 5-6"/></svg>Club excursions</li>
        <li><svg width="14" height="14" viewBox="0 0 24 24" fill="none" stroke="#e0262b" stroke-width="2.5"><rect x="3" y="3" width="18" height="18" rx="3"/><path d="M8 12l3 3 5-6"/></svg>Corporate events</li>
        <li><svg width="14" height="14" viewBox="0 0 24 24" fill="none" stroke="#e0262b" stroke-width="2.5"><rect x="3" y="3" width="18" height="18" rx="3"/><path d="M8 12l3 3 5-6"/></svg>Weddings &amp; celebrations</li>
        <li><svg width="14" height="14" viewBox="0 0 24 24" fill="none" stroke="#e0262b" stroke-width="2.5"><rect x="3" y="3" width="18" height="18" rx="3"/><path d="M8 12l3 3 5-6"/></svg>Airport transfers</li>
      </ul>
      <a class="btn btn-block" href="#">Request Quote</a>
    </article>
  </div>
</section>

<section class="section destinations">
  <h2 class="section-title">Our Destinations</h2>
  <p class="section-sub">Discover the most beautiful places in Europe with us</p>
  <div class="dest-grid">
    <div class="dest-card"><div class="media" role="img" aria-label="Swiss Alps with a coach on a mountain road" style="background:linear-gradient(160deg,#7f93a6,#4d5e52)"></div><span>Swiss Alps</span></div>
    <div class="dest-card"><div class="media" role="img" aria-label="Italian lake in evening light" style="background:linear-gradient(160deg,#3c4a57,#7d6c52)"></div><span>Italian Lakes</span></div>
    <div class="dest-card"><div class="media" role="img" aria-label="Historic old town of an Austrian city" style="background:linear-gradient(160deg,#8c8678,#4f4a44)"></div><span>Austrian Cities</span></div>
    <div class="dest-card"><div class="media" role="img" aria-label="Flower meadow at a seasonal market" style="background:linear-gradient(160deg,#9a9588,#6b4a3e)"></div><span>Christmas Markets</span></div>
  </div>
</section>

<section class="section fleet">
  <h2 class="section-title">Our Vehicle Fleet</h2>
  <p class="section-sub">Modern, comfortable coaches for every occasion</p>
  <div class="fleet-grid">
    <div class="fleet-card"><div class="media" role="img" aria-label="Driver team in front of a large touring coach" style="background:linear-gradient(160deg,#6f8196,#3a4350)"></div><div class="caption"><strong>50 Seats Coaches</strong><small>For larger groups and long tours</small></div></div>
    <div class="fleet-card"><div class="media" role="img" aria-label="Driver team in front of a midsize coach" style="background:linear-gradient(160deg,#5c7fa3,#334456)"></div><div class="caption"><strong>25 Seats Coaches</strong><small>Perfect for clubs and smaller groups</small></div></div>
  </div>
</section>

<section class="section testimonials">
  <h2 class="section-title">What Our Customers Say</h2>
  <p class="section-sub">Trust from years of experience and satisfied customers</p>
  <div class="quote-grid">
    <article class="quote-card">
      <div class="stars"><svg width="70" height="12" viewBox="0 0 70 12" fill="#f5b301"><path id="s" d="M6 0l1.8 3.8 4.2.5-3.1 2.9.8 4.2L6 9.3 2.3 11.4l.8-4.2L0 4.3l4.2-.5z"/><use href="#s" x="14"/><use href="#s" x="28"/><use href="#s" x="42"/><use href="#s" x="56"/></svg></div>
      <p>"We have travelled with them for ten years. The service is always kind and the drivers are excellent."</p>
      <div class="author">Maria Brunner</div><div class="place">Chur</div>
    </article>
    <article class="quote-card">
      <div class="stars"><svg width="70" height="12" viewBox="0 0 70 12" fill="#f5b301"><use href="#s"/><use href="#s" x="14"/><use href="#s" x="28"/><use href="#s" x="42"/><use href="#s" x="56"/></svg></div>
      <p>"Perfect organisation and very reliable. Thanks to our club trip, everyone was truly happy."</p>
      <div class="author">Hans Caduff</div><div class="place">Ilanz</div>
    </article>
    <article class="quote-card">
      <div class="stars"><svg width="70" height="12" viewBox="0 0 70 12" fill="#f5b301"><use href="#s"/><use href="#s" x="14"/><use href="#s" x="28"/><use href="#s" x="42"/><use href="#s" x="56"/></svg></div>
      <p>"The trip to Como was wonderful for seniors. Thank you for the wonderful experience!"</p>
      <div class="author">Elisabeth Sutter</div><div class="place">Thusis</div>
    </article>
  </div>
</section>

<section class="section contact">
  <h2 class="section-title">Contact &amp; Opening Hours</h2>
  <p class="section-sub">We are here for you</p>
  <div class="contact-grid">
    <article class="contact-card">
      <h3>Opening Hours</h3>
      <div class="hours-row"><b>Monday – Friday</b><span>08:00 – 18:00</span></div>
      <div class="hours-row"><b>Saturday</b><span>09:00 – 12:00</span></div>
      <div class="hours-row"><b>Sunday</b><span>Closed</span></div>
      <p class="notice">Annual Program 2024</p>
      <a class="btn btn-small" href="#">Download PDF</a>
    </article>
    <article class="contact-card">
      <h3>Contact Information</h3>
      <div class="info-item"><b>Address</b>Reisebüro Lenz Vals, Talstrasse 12, 7132 Vals</div>
      <div class="info-item"><b>Phone</b>+41 81 555 24 60</div>
      <div class="info-item"><b>Email</b>info@lenzvals-beispiel.ch</div>
      <a class="btn btn-block" href="#">Request Quote</a>
    </article>
  </div>
</section>

<footer class="site-footer">
  <div class="footer-grid">
    <div class="footer-brand">
      <a class="brand" href="#"><span class="brand-mark"></span>Lenz Vals</a>
      <p>Your trusted partner for bus tours throughout Europe since many years.</p>
    </div>
    <div>
      <h4>Our Services</h4>
      <ul><li>Day trips</li><li>Multi-day tours</li><li>Music tours</li><li>Bus rental</li></ul>
    </div>
    <div>
      <h4>Service</h4>
      <ul><li>About us</li><li>Gallery</li><li>Fleet</li><li>Annual program</li></ul>
    </div>
    <div>
      <h4>Contact</h4>
      <ul><li>Talstrasse 12</li><li>7132 Vals</li><li>+41 81 555 24 60</li><li>www.lenzvals-beispiel.ch</li></ul>
    </div>
  </div>
  <p class="copyright">© 2024 Reisebüro Lenz Vals. All rights reserved.</p>
</footer>

</body>
</html>
```